Fancy looking Inspection Postcard

Postcard needed for customers to inspect their product once it is delivered. We'll be giving them the steps for inspecting their product and to contact us if any issues arise. Would like to see something that sticks out but uses our company's colors. Would like to see creativity. Possibly utilizing the diamond steel background like we have in our logo.

Target Market(s)

Customers of our manufacturing shop

Industry/Entity Type

Manufacturing - metal wall art, custom products

Requirements
Must have
• our colors and logo
Nice to have
• get creative. i like creativity

```html
<!DOCTYPE html>
<html lang="en">
<head>
<meta charset="utf-8">
<title>Birch Creek Fabrication – Inspection Postcard</title>
<link rel="stylesheet" href="https://fonts.googleapis.com/css2?family=Poppins:wght@300;400;600;700;800;900&display=swap">
<style>
  :root {
    --sand: #e0926f;
    --salmon: #f78676;
    --panel: #d9936f;
    --plum: #5f516c;
    --teal: #067f7b;
    --teal-ink: #16857d;
    --coral-line: #ef8a74;
  }
  * { margin: 0; padding: 0; box-sizing: border-box; }
  html, body { width: 801px; height: 1200px; overflow: hidden; background: var(--sand); }
  body { position: relative; font-family: "Poppins", sans-serif; }

  .postcard { position: absolute; left: 0; width: 801px; height: 530px; background: var(--salmon); overflow: hidden; }
  .postcard--front { top: 51px; }
  .postcard--back { top: 654px; }

  .postcard__panel { position: absolute; left: 32px; top: 35px; width: 370px; height: 474px; background: var(--panel); }
  .postcard__shapes { position: absolute; inset: 0; }

  .brand { position: absolute; left: 78px; top: 73px; display: flex; align-items: center; gap: 9px; }
  .brand__mark { width: 36px; height: 40px; background: var(--teal-ink); }
  .brand__name { font-weight: 700; font-size: 12.5px; line-height: 1.1; letter-spacing: 0.5px; color: var(--teal-ink); text-transform: uppercase; }

  .headline { position: absolute; left: 56px; top: 165px; color: var(--teal-ink); text-transform: uppercase; }
  .headline__line { display: block; font-weight: 300; font-size: 43px; line-height: 40px; letter-spacing: 2px; }
  .headline__line--strong { font-weight: 900; letter-spacing: 1px; }

  .stamp-box { position: absolute; left: 640px; top: 148px; width: 110px; height: 110px; border: 1px solid var(--coral-line); }
  .address-line { position: absolute; right: 49px; height: 1px; background: var(--coral-line); }

  .review-note { position: absolute; left: 404px; top: 443px; font-weight: 300; font-size: 16px; line-height: 20px; color: var(--coral-line); }
  .review-note__contacts { display: flex; align-items: center; gap: 6px; }
  .review-note__contacts svg { width: 16px; height: 16px; }
  .review-note__gap { width: 4px; }

  .guide { position: absolute; left: 480px; top: 122px; width: 294px; }
  .guide__title { font-weight: 400; font-size: 16px; color: var(--coral-line); text-align: right; letter-spacing: 0.3px; margin-right: -6px; margin-bottom: 10px; }
  .guide__step { display: flex; justify-content: flex-end; align-items: center; gap: 8px; height: 50px; }
  .guide__text { text-align: right; }
  .guide__heading { font-weight: 800; font-size: 13px; line-height: 14px; color: var(--teal); text-transform: uppercase; letter-spacing: -0.3px; }
  .guide__question { font-weight: 700; font-size: 11.5px; line-height: 11px; color: var(--coral-line); letter-spacing: 0.3px; }
  .guide__question--wide { letter-spacing: 1.8px; }
  .guide__num { width: 42px; height: 40px; border: 2px solid var(--teal); border-radius: 5px; display: flex; align-items: center; justify-content: center; font-weight: 600; font-size: 25px; color: var(--teal); }

  .contact { position: absolute; left: 515px; top: 390px; color: var(--coral-line); }
  .contact__title { font-weight: 400; font-size: 16px; margin-bottom: 12px; }
  .contact__row { display: flex; align-items: center; gap: 13px; margin-left: 57px; height: 25.5px; font-weight: 300; font-size: 12px; }
  .contact__row svg { width: 14px; height: 14px; }
</style>
</head>
<body>

<section class="postcard postcard--front">
  <div class="postcard__panel"></div>
  <svg class="postcard__shapes" viewBox="0 0 801 530" aria-hidden="true">
    <polygon points="491,0 801,0 801,530 277,530" fill="var(--plum)"/>
    <polygon points="407,8 527,8 277,530 283,514" fill="var(--teal)"/>
  </svg>

  <div class="brand"><span class="brand__mark"></span><span class="brand__name">Birch Creek<br>Fabrication</span></div>

  <h1 class="headline">
    <span class="headline__line">Did we</span>
    <span class="headline__line">do a</span>
    <span class="headline__line headline__line--strong">Good job?</span>
  </h1>

  <div class="stamp-box"></div>
  <div class="address-line" style="top:306px;left:489px"></div>
  <div class="address-line" style="top:345px;left:472px"></div>
  <div class="address-line" style="top:380px;left:456px"></div>
  <div class="address-line" style="top:413px;left:440px"></div>

  <div class="review-note">
    <p>If you think so, leave us a review on Reviewly.</p>
    <p>If not, Please let us know.</p>
    <p class="review-note__contacts">
      <svg viewBox="0 0 16 16"><rect x="1" y="3" width="14" height="10" fill="var(--coral-line)"/><path d="M1 3l7 6 7-6" fill="none" stroke="var(--plum)" stroke-width="1"/></svg>
      <span>info@birchfab.com</span><span class="review-note__gap"></span>
      <svg viewBox="0 0 16 16"><path d="M4 1l3 3-2 2c1 2 3 4 5 5l2-2 3 3-2 2C7 14 2 9 2 3z" fill="var(--coral-line)"/></svg>
      <span>208-555-0147</span>
    </p>
  </div>
</section>

<section class="postcard postcard--back">
  <div class="postcard__panel"></div>
  <svg class="postcard__shapes" viewBox="0 0 801 530" aria-hidden="true">
    <polygon points="491,0 801,0 801,530 277,530" fill="var(--plum)"/>
    <polygon points="407,8 527,8 277,530 283,514" fill="var(--teal)"/>
  </svg>

  <div class="brand"><span class="brand__mark"></span><span class="brand__name">Birch Creek<br>Fabrication</span></div>

  <h2 class="headline">
    <span class="headline__line">Did we</span>
    <span class="headline__line">do a</span>
    <span class="headline__line headline__line--strong">Good job?</span>
  </h2>

  <div class="guide">
    <h3 class="guide__title">PRODUCT INSPECTION GUIDELINES</h3>
    <div class="guide__step">
      <div class="guide__text"><p class="guide__heading">Inspect general shape</p><p class="guide__question">Is it what you expected?<br>Is it bent or disoriented?</p></div>
      <span class="guide__num">1</span>
    </div>
    <div class="guide__step">
      <div class="guide__text"><p class="guide__heading">Inspect the welds if there are any</p><p class="guide__question guide__question--wide">Do they look clean?<br>Are there any gaps?</p></div>
      <span class="guide__num">2</span>
    </div>
    <div class="guide__step">
      <div class="guide__text"><p class="guide__heading">Inspect the finish</p><p class="guide__question">Are there any areas not finished?<br>Are the colors what you expected?</p></div>
      <span class="guide__num">3</span>
    </div>
    <div class="guide__step">
      <div class="guide__text"><p class="guide__heading">Check for functionality</p><p class="guide__question">Does it work the way you want it to?<br>Is it what you expected?</p></div>
      <span class="guide__num">4</span>
    </div>
  </div>

  <div class="contact">
    <h3 class="contact__title">CONTACT US</h3>
    <p class="contact__row"><svg viewBox="0 0 16 16"><path d="M4 1l3 3-2 2c1 2 3 4 5 5l2-2 3 3-2 2C7 14 2 9 2 3z" fill="var(--coral-line)"/></svg>(208) 555-0182</p>
    <p class="contact__row"><svg viewBox="0 0 16 16"><rect x="1" y="3" width="14" height="10" fill="var(--coral-line)"/><path d="M1 3l7 6 7-6" fill="none" stroke="var(--plum)" stroke-width="1"/></svg>orders@birchfab.com</p>
    <p class="contact__row"><svg viewBox="0 0 16 16"><circle cx="8" cy="8" r="7" fill="var(--coral-line)"/><path d="M1 8h14M8 1c-3 4-3 10 0 14M8 1c3 4 3 10 0 14" fill="none" stroke="var(--plum)" stroke-width="1"/></svg>www.birchfab.com/contact</p>
  </div>
</section>

</body>
</html>
```